Conference program advertisement

Our business www.clinicledger.com.au is a good sponsor of the conference program run by the Southern Pacific Guild of Perioperative Physicians (SPGPP) here in Western Australia.
We have been running the same ad for a while and so we could do with a fresh new presence.
We have a conference banner and other signage that we'll use at the trade show so we're not looking to rebrand. Just looking for a new ad.
Specification is full colour A4, high res PDF
(Because I'm using my phone to create this job, I cannot seem to upload the existing ad. I'll do do ASAP.)

Target Market(s)

Specialist doctors

Industry/Entity Type

Trade

Font styles to use
Sans Serif

Colors

Designer to choose colors to be used in the design.

Requirements
Must have
• A4
Existing logo and colour scheme

```html
<!DOCTYPE html>
<html lang="en">
<head>
<meta charset="utf-8">
<title>Clinic Ledger Services – Conference Advertisement</title>
<link rel="stylesheet" href="https://fonts.googleapis.com/css2?family=Oswald:wght@300;400&family=Roboto:wght@300;400;700&display=swap">
<style>
  :root {
    --red-deep: #8e0d12;
    --red-main: #d0161c;
    --red-bright: #e8232a;
    --red-dark: #6e0a0e;
    --white: #ffffff;
    --ink: #222222;
    --yellow: #ffe600;
    --pale: #f3c9ca;
  }
  * { margin: 0; padding: 0; box-sizing: border-box; }
  html, body { width: 848px; height: 1200px; overflow: hidden; background: var(--white); }
  .ad {
    position: relative;
    width: 848px;
    height: 1200px;
    overflow: hidden;
    background: radial-gradient(ellipse at 20% 20%, var(--red-bright) 0%, var(--red-main) 45%, var(--red-deep) 100%);
    font-family: "Roboto", Arial, sans-serif;
    color: var(--white);
  }
  .hero-photo {
    position: absolute;
    left: 0; top: 0;
    width: 848px; height: 570px;
    background:
      radial-gradient(ellipse at 72% 40%, rgba(240,120,120,0.55) 0%, rgba(200,40,45,0) 55%),
      linear-gradient(180deg, #b5151b 0%, #a81218 60%, #c4181e 100%);
  }
  .hero-photo::after {
    content: "";
    position: absolute; left: 0; right: 0; bottom: 0; height: 90px;
    background: linear-gradient(180deg, rgba(216,28,34,0) 0%, rgba(216,28,34,0.9) 100%);
  }
  .headline {
    position: absolute;
    left: 78px; top: 104px;
    font-family: "Oswald", "Arial Narrow", sans-serif;
    font-weight: 400;
    text-transform: uppercase;
    line-height: 0.98;
    letter-spacing: -0.5px;
  }
  .headline span { display: block; }
  .headline .small { font-size: 42px; }
  .headline .mid { font-size: 80px; line-height: 0.95; }
  .headline .big { font-size: 136px; line-height: 0.9; }
  .intro {
    position: absolute;
    left: 63px; top: 620px;
    width: 450px;
  }
  .intro .lead {
    font-weight: 300;
    font-size: 27.5px;
    line-height: 1.17;
    margin-bottom: 10px;
  }
  .intro .body {
    font-weight: 700;
    font-size: 12.6px;
    line-height: 1.55;
  }
  .services {
    position: absolute;
    left: 548px; top: 626px;
    list-style: none;
    font-weight: 700;
    font-size: 9.6px;
    letter-spacing: 0.4px;
    line-height: 20px;
    text-transform: uppercase;
    width: 250px;
  }
  .services li { position: relative; padding-left: 16px; }
  .services li::before {
    content: "";
    position: absolute; left: 0; top: 8px;
    width: 4px; height: 4px; border-radius: 50%;
    background: var(--pale);
  }
  .brand {
    position: absolute;
    left: 600px; top: 996px;
    display: flex; align-items: center; gap: 14px;
  }
  .brand-mark {
    width: 78px; height: 78px;
    background: #d9d9d9;
    border-radius: 4px;
  }
  .brand-name {
    font-family: "Oswald", "Arial Narrow", sans-serif;
    font-weight: 300;
    font-size: 21px;
    line-height: 1.05;
    text-transform: uppercase;
    color: var(--white);
  }
  .contact-card {
    position: absolute;
    left: 0; top: 1094px;
    width: 509px; height: 67px;
    background: var(--white);
    color: var(--ink);
    font-size: 10px;
    line-height: 1.4;
    padding: 10px 0 0 63px;
  }
  .postal {
    position: absolute;
    left: 556px; top: 1100px;
    text-align: right;
    width: 232px;
    font-size: 13px;
    line-height: 1.45;
  }
  .postal .po { font-weight: 700; }
  .postal .web { font-weight: 700; font-size: 14.5px; color: var(--yellow); }
</style>
</head>
<body>
<div class="ad">
  <div class="hero-photo" role="img" aria-label="Red-toned photograph of a surgeon in scrubs and mask writing notes beside anaesthetic equipment in an operating theatre"></div>

  <h1 class="headline">
    <span class="small">Is administration</span>
    <span class="small">eating up your</span>
    <span class="mid">Valuable</span>
    <span class="big">Time?</span>
  </h1>

  <section class="intro">
    <p class="lead">Admin can consume a large amount of time for doctors working in private practice.</p>
    <p class="body">From generating accounts to chasing up bad debts, from sitting on hold with health funds, or trawling through remittance advices to getting accreditation papers and submitting provider number applications properly – we’re sure you would prefer to focus on being a doctor rather than worrying about paperwork and piles of admin. Clinic Ledger Services is here to help – contact us today if you’re ready to remove the burden of admin.</p>
  </section>

  <ul class="services">
    <li>Private billing</li>
    <li>VMP billing</li>
    <li>Practice management</li>
    <li>Organise lists</li>
    <li>Cover lists</li>
    <li>Banking</li>
    <li>Medicare and health fund<br>registrations</li>
    <li>Fee estimates and informed<br>financial consent</li>
    <li>Direct Bill and credit card payments</li>
    <li>Electronic claiming to<br>health funds</li>
    <li>GST reporting</li>
    <li>Hospital accreditations</li>
  </ul>

  <div class="brand">
    <div class="brand-mark"></div>
    <div class="brand-name">Clinic<br>Ledger<br>Services</div>
  </div>

  <div class="contact-card">
    <p>Sam Whitford Mobile +61 400 555 218</p>
    <p>Office 08 6000 1420 • Fax 08 6000 1421</p>
    <p>First Floor, Unit 12, 450 Harbour Road, West Perth, WA, 6005</p>
  </div>

  <div class="postal">
    <p class="po">PO Box 310, West Perth WA 6872</p>
    <p>sam@clinicledger.com.au</p>
    <p class="web">www.clinicledger.com.au</p>
  </div>
</div>
</body>
</html>
```